Brelvo Pizza & Pasta Takeaway Flyer

Our takeaway shop needs a well designed flyer for print and letter box distribution. Design to have a clear list of menu, Specials, contact details. If menu doesn't fit into A4, we won't mind going upto extended A4. I have attached draft copy of our menu and list of item in excel. Please add 5mm Bleed to the flyer.
Flyer will get printed on 115gsm Gloss stock.

```html
<!DOCTYPE html>
<html lang="en">
<head>
<meta charset="utf-8">
<title>Brelvo Pizza &amp; Pasta – Takeaway Menu</title>
<link href="https://fonts.googleapis.com/css2?family=Oswald:wght@500;600&family=Roboto+Condensed:wght@400;700&display=swap" rel="stylesheet">
<style>
  :root{
    --backdrop:#ece6dc;
    --slate:#2e3845;
    --slate-mark:#374350;
    --red:#c4392f;
    --green:#6fb53e;
    --ink:#ffffff;
    --ink-dim:#c9d0d8;
    --leader:#8c96a2;
    --pizza:#c9773b;
    --pasta:#e8d7b0;
  }
  *{box-sizing:border-box;margin:0;padding:0}
  html,body{width:1200px;height:900px;overflow:hidden;background:var(--backdrop)}
  body{display:flex;align-items:center;justify-content:center;font-family:"Roboto Condensed",sans-serif;color:var(--ink)}
  .flyer{width:1160px;height:860px;background:var(--slate);display:grid;grid-template-columns:1fr 1fr 1fr 1fr;gap:26px;padding:22px 28px;position:relative;overflow:hidden}
  .brand-mark{position:absolute;left:50%;top:50%;transform:translate(-50%,-50%);font-family:"Oswald",sans-serif;font-weight:600;font-size:92px;line-height:1;color:var(--slate-mark);white-space:nowrap;pointer-events:none;z-index:0;text-align:center}
  .column{display:flex;flex-direction:column;gap:4px;min-width:0;position:relative;z-index:1}
  .section-bar{background:var(--red);font-family:"Oswald",sans-serif;font-weight:600;font-size:15px;letter-spacing:1px;text-transform:uppercase;padding:2px 10px;margin:6px 0 4px;display:flex;gap:10px;align-items:baseline}
  .section-bar small{font-size:10px;font-weight:500;letter-spacing:.3px;text-transform:none}
  .item{display:flex;align-items:baseline;gap:4px;font-size:12.5px;font-weight:700;letter-spacing:.2px}
  .item .leader{flex:1;border-bottom:2px dotted var(--leader);transform:translateY(-3px)}
  .desc{font-size:8.5px;color:var(--ink-dim);line-height:1.15;margin-top:-1px}
  .entry{display:flex;flex-direction:column;gap:1px}
  .note{font-size:9.5px;color:var(--ink-dim);margin:1px 0}
  .note.strong{font-size:11.5px;color:var(--ink);font-weight:700}
  .price-band{background:var(--green);display:grid;grid-template-columns:1.4fr 1fr 1fr 1fr;align-items:end;padding:3px 8px;margin:6px 0 4px;font-weight:700}
  .price-band .tier{font-family:"Oswald",sans-serif;font-size:12px;letter-spacing:.5px;text-transform:uppercase}
  .price-band .size{text-align:center;font-size:9px;font-weight:400;line-height:1}
  .price-band .size b{display:block;font-size:13px;font-weight:700;line-height:1.1}
  .pizza-name{display:block;font-size:12.5px;font-weight:700}
  .photo{border-radius:6px;flex-shrink:0}
  .photo-pizza{height:130px;width:130px;border-radius:50%;align-self:center;margin-bottom:2px;background:radial-gradient(circle at 50% 50%,#e0a15a 0,var(--pizza) 55%,#8a4a22 100%)}
  .photo-pasta{margin-top:auto;height:190px;background:radial-gradient(circle at 50% 50%,var(--pasta) 0,#cfb98a 50%,#1d2228 72%)}
  .specials{margin-top:auto;border:2px solid var(--red);padding:6px 8px;display:flex;flex-direction:column;gap:3px}
  .specials .item{font-size:11.5px}
  .contact{margin-top:8px;display:flex;flex-direction:column;gap:3px}
  .contact .shop-name{font-family:"Oswald",sans-serif;font-weight:600;font-size:17px;letter-spacing:.5px;color:var(--ink)}
  .contact-line{display:flex;align-items:center;gap:6px;font-size:11.5px;font-weight:700}
  .contact-line svg{width:12px;height:12px;fill:var(--red);flex-shrink:0}
  .contact .note{margin-top:2px}
</style>
</head>
<body>
<main class="flyer">
  <div class="brand-mark" aria-hidden="true">Brelvo<br>Pizza &amp; Pasta</div>

  <section class="column">
    <h2 class="section-bar">Starter</h2>
    <div class="item"><span>Garlic Bread</span><span class="leader"></span><span>$3.95</span></div>
    <div class="item"><span>Cheesy Garlic Bread</span><span class="leader"></span><span>$5.50</span></div>
    <div class="entry"><div class="item"><span>Sweet Chilli Cheese Pizza</span><span class="leader"></span><span>$7.95</span></div><p class="desc">Sweet Chilli Sauce Base topped with Cheese &amp; Herbs</p></div>
    <div class="entry"><div class="item"><span>Chips (Lge - 2$)</span><span class="leader"></span><span>$4.95</span></div><p class="desc">with Tomato Sauce</p></div>
    <div class="item"><span>Chips &amp; Gravy</span><span class="leader"></span><span>$6.95</span></div>
    <div class="item"><span>Beer Battered Chips</span><span class="leader"></span><span>$5.95</span></div>
    <div class="entry"><div class="item"><span>Curly Fries (Lge - 2.5$)</span><span class="leader"></span><span>$6.95</span></div><p class="desc">with Ranch Dip</p></div>
    <div class="entry"><div class="item"><span>Sweet Potato Chips</span><span class="leader"></span><span>$6.50</span></div><p class="desc">with Garlic Aioli Sauce</p></div>
    <div class="entry"><div class="item"><span>Onion Rings</span><span class="leader"></span><span>$4.95</span></div><p class="desc">with Ranch Dip</p></div>
    <div class="entry"><div class="item"><span>Chicken Nuggets (8 Pcs)</span><span class="leader"></span><span>$6.95</span></div><p class="desc">with Tomato Sauce</p></div>
    <div class="item"><span>Popper Squid</span><span class="leader"></span><span>$7.95</span></div>
    <div class="entry"><div class="item"><span>Beef Chilli</span><span class="leader"></span><span>$7.95</span></div><p class="desc">with Lemon Wedge</p></div>
    <div class="entry"><div class="item"><span>Chicken Lollipop</span><span class="leader"></span><span>$7.95</span></div><p class="desc">with Garlic Aioli Sauce</p></div>
    <p class="note strong">** Add Extra Sauce 0.75 $</p>

    <h2 class="section-bar">Main <small>(Served with Chips &amp; Garden Salad)</small></h2>
    <div class="item"><span>Chicken Schnitzel with Gravy</span><span class="leader"></span><span>$16</span></div>
    <div class="item"><span>Veal Schnitzel with Gravy</span><span class="leader"></span><span>$16</span></div>
    <div class="item"><span>Chicken Parmigiana</span><span class="leader"></span><span>$17</span></div>
    <div class="entry"><div class="item"><span>Three Cheese Parmigiana</span><span class="leader"></span><span>$17</span></div><p class="desc">Topped with Parmesan, Mozzarella, Bocconcini &amp; Herbs</p></div>
    <div class="entry"><div class="item"><span>Hawaiian Parmigiana</span><span class="leader"></span><span>$17</span></div><p class="desc">Topped with Cheese, Ham, Pineapple &amp; Herbs</p></div>
    <div class="entry"><div class="item"><span>Mexican Parmigiana</span><span class="leader"></span><span>$17</span></div><p class="desc">Topped with Cheese, Roasted Capsicum, Jalapenos &amp; Herbs</p></div>
    <div class="entry"><div class="item"><span>Marinara Parmigiana</span><span class="leader"></span><span>$19</span></div><p class="desc">Topped with Cheese, Seafood Mix &amp; Herbs</p></div>
    <div class="entry"><div class="item"><span>Creamy Garlic Prawn</span><span class="leader"></span><span>$19</span></div><p class="desc">Tiger Prawn, Garlic, White Wine, Spices &amp; Herbs Pan fried with Creamy Sauce</p></div>

    <h2 class="section-bar">Galzone</h2>
    <p class="desc">Folded Pizza, Rolled &amp; Cooked, Sealing in All Flavours. Simply Select from Menu</p>
    <div class="item"><span>Classic Calzone</span><span class="leader"></span><span>$16</span></div>
    <div class="item"><span>Premium Calzone</span><span class="leader"></span><span>$18</span></div>
  </section>

  <section class="column">
    <h2 class="section-bar">Garlic Sub $9.95</h2>
    <div class="entry"><span class="pizza-name">Pulled Beef</span><p class="desc">Cheese, Pulled Beef, Salami, Onion, Mushroom with BBQ Sauce</p></div>
    <div class="entry"><span class="pizza-name">Chicken</span><p class="desc">Cheese, Seasoned Chicken, Tomato, Onion, Feta with Sweet Chilli</p></div>
    <div class="entry"><span class="pizza-name">Veg</span><p class="desc">Cheese, Tomato, Onion, Mushroom, Capsicum, Pineapple with Garlic</p></div>
    <div class="entry"><span class="pizza-name">Meat</span><p class="desc">Cheese, Ham, Pepperoni, Salami, Sausage with BBQ Sauce</p></div>
    <div class="entry"><span class="pizza-name">Bacon &amp; Chicken</span><p class="desc">Cheese, Seasoned Chicken, Bacon, Mushroom with Peri Peri Sauce</p></div>

    <h2 class="section-bar">Pizza</h2>
    <div class="price-band"><span class="tier">Lite</span><span class="size">Small<b>$9</b></span><span class="size">Large<b>$15</b></span><span class="size">Family<b>$20</b></span></div>
    <div class="entry"><span class="pizza-name">Hawaiian</span><p class="desc">Cheese, Ham &amp; Pineapple</p></div>
    <div class="entry"><span class="pizza-name">Margherita</span><p class="desc">Cheese, Tomatoes, Basil &amp; Oregano</p></div>
    <div class="entry"><span class="pizza-name">Mozzy</span><p class="desc">Cheese, Garlic, Basil &amp; Oregano</p></div>
    <div class="entry"><span class="pizza-name">New Yorker</span><p class="desc">Pepperoni, Basil &amp; Oregano</p></div>
    <div class="entry"><span class="pizza-name">Veggie</span><p class="desc">Onion, Tomato, Mushroom, Capsicum, Olives, Pineapple, Basil &amp; Oregano</p></div>

    <div class="price-band"><span class="tier">Classic</span><span class="size">Small<b>$11</b></span><span class="size">Large<b>$17</b></span><span class="size">Family<b>$22</b></span></div>
    <div class="entry"><span class="pizza-name">Supreme</span><p class="desc">Cheese, Pepperoni, Ham, Beef, Onion, Olives, Capsicum, Pineapple &amp; Mushroom</p></div>
    <div class="entry"><span class="pizza-name">Meat Lovers</span><p class="desc">Cheese, Pepperoni, Salami, Ham, Bacon, Sausage with BBQ Sauce</p></div>
    <div class="entry"><span class="pizza-name">Ozzy</span><p class="desc">Cheese, Sausage, Bacon, Onion &amp; Egg</p></div>
    <div class="entry"><span class="pizza-name">BBQ Chicken</span><p class="desc">Cheese, Chicken, Bacon, Mushroom &amp; BBQ Sauce</p></div>
    <div class="entry"><span class="pizza-name">Tropical Chicken</span><p class="desc">Cheese, Chicken, Ham, Pineapple</p></div>
    <div class="entry"><span class="pizza-name">Outback</span><p class="desc">Cheese, Ham, Salami, Bacon, Mushroom &amp; Onion</p></div>
    <div class="entry"><span class="pizza-name">Spicy Pizza</span><p class="desc">Cheese, Pepperoni, Onion, Jalapenos &amp; Chilli Flakes</p></div>
    <div class="entry"><span class="pizza-name">Mexican</span><p class="desc">Cheese, Beef, Pepperoni, Onion, Roasted Capsicum, Chilli &amp; Jalapenos</p></div>
    <div class="entry"><span class="pizza-name">Capricciosa</span><p class="desc">Cheese, Ham, Salami, Mushroom, Tomato &amp; Olives</p></div>
    <div class="entry"><span class="pizza-name">Veg Supreme</span><p class="desc">Cheese, Onion, Mushroom, Roasted Capsicum, Pineapple, Feta, Jalapeno &amp; Chilli</p></div>
    <div class="entry"><span class="pizza-name">Four Cheese</span><p class="desc">Cheese, Feta, Bocconcini, Parmesan &amp; Basil</p></div>
  </section>

  <section class="column">
    <div class="photo photo-pizza" role="img" aria-label="Photo of a sliced mushroom pizza"></div>
    <div class="price-band"><span class="tier">Premium</span><span class="size">Small<b>$13</b></span><span class="size">Large<b>$19</b></span><span class="size">Family<b>$25</b></span></div>
    <div class="entry"><span class="pizza-name">Garden Gourmet</span><p class="desc">Cheese, Sundried Tomato, Mushroom, Onion, Roasted Capsicum, Olives, Cherry Tomato, Spinach, Bocconcini &amp; Basil</p></div>
    <div class="entry"><span class="pizza-name">Paneer Tikka</span><p class="desc">Cheese, Marinated Paneer, Onion, Tomato, Capsicum, Olives &amp; Coriander</p></div>
    <div class="entry"><span class="pizza-name">Pesto Chicken</span><p class="desc">Cheese, Chicken, Sundried Tomato, Onion, Feta &amp; Parsley</p></div>
    <div class="entry"><span class="pizza-name">Butter Chicken</span><p class="desc">Cheese, Butter Chicken, Onion, Capsicum, Coriander, Cashew &amp; Mint Sauce</p></div>
    <div class="entry"><span class="pizza-name">Meat &amp; Chicken</span><p class="desc">Cheese, Pepperoni, Chicken, Salami, Roasted Capsicum, Onion, Bacon &amp; Sausage</p></div>
    <div class="entry"><span class="pizza-name">Mediterranean</span><p class="desc">Pulled Beef, Roasted Capsicum, Spinach, Olives, Feta &amp; Oregano</p></div>
    <div class="entry"><span class="pizza-name">The Lot</span><p class="desc">Cheese, Ham, Salami, Pulled Beef, Sausage, Mushroom, Onion, Capsicum, Pineapple</p></div>

    <div class="price-band"><span class="tier">Premium</span><span class="size">Small<b>$14</b></span><span class="size">Large<b>$21</b></span><span class="size">Family<b>$28</b></span></div>
    <div class="entry"><span class="pizza-name">The Pacific</span><p class="desc">Cheese, Garlic, Prawn, Mushroom, Roasted Capsicum &amp; Chilli Flakes</p></div>
    <div class="entry"><span class="pizza-name">Reef n Turf</span><p class="desc">Cheese, Beef, Prawn, Onion, Mushroom, Capsicum, Olives &amp; Garlic Sauce</p></div>
    <div class="entry"><span class="pizza-name">Prawn &amp; Garlic</span><p class="desc">Prawn, Cherry Tomato, Spinach, Bocconcini &amp; Garlic Sauce</p></div>
    <p class="note">** Gluten free base available in large size, Extra $3</p>
    <p class="note">** Extra toppings: Small $1, Large $2, Family $3</p>

    <div class="specials">
      <h2 class="section-bar">Specials</h2>
      <div class="item"><span>2 Large Classic Pizzas + Garlic Bread</span><span class="leader"></span><span>$35</span></div>
      <div class="item"><span>Family Pizza + Any Pasta + Chips</span><span class="leader"></span><span>$39</span></div>
      <div class="item"><span>Any Pasta + Garlic Bread</span><span class="leader"></span><span>$18</span></div>
    </div>
  </section>

  <section class="column">
    <h2 class="section-bar">Pasta</h2>
    <div class="entry"><div class="item"><span>Napolitana</span><span class="leader"></span><span>$14</span></div><p class="desc">Tomato, Onion, Garlic &amp; Special Italian Herbs in Red Pasta Sauce</p></div>
    <div class="entry"><div class="item"><span>Vegetaria</span><span class="leader"></span><span>$16</span></div><p class="desc">Mushroom, Tomato, Onion, Capsicum, Olives &amp; Herbs in Red Pasta Sauce</p></div>
    <div class="entry"><div class="item"><span>Bolognese</span><span class="leader"></span><span>$16</span></div><p class="desc">Traditional Beef, Onion &amp; Special Italian Herbs in Red Pasta Sauce</p></div>
    <div class="entry"><div class="item"><span>Carbonara</span><span class="leader"></span><span>$16</span></div><p class="desc">Bacon, Egg, Mushroom &amp; Onion in a Creamy White Sauce</p></div>
    <div class="entry"><div class="item"><span>Alfa Pama</span><span class="leader"></span><span>$16</span></div><p class="desc">Ham, Mushroom in Creamy White Sauce</p></div>
    <div class="entry"><div class="item"><span>Chicken Carbonara</span><span class="leader"></span><span>$16</span></div><p class="desc">Chicken, Bacon, Mushroom &amp; Onion in a Creamy White Sauce</p></div>
    <div class="entry"><div class="item"><span>Chicken Pesto</span><span class="leader"></span><span>$16</span></div><p class="desc">Chicken, Sundried Tomato, Pesto in Creamy Sauce</p></div>
    <div class="entry"><div class="item"><span>Greek Chicken</span><span class="leader"></span><span>$16</span></div><p class="desc">Chicken, Spinach, Olives, Feta in Creamy White Sauce</p></div>
    <div class="entry"><div class="item"><span>Garlic Prawn</span><span class="leader"></span><span>$16</span></div><p class="desc">Prawn, Garlic, Chilli in Creamy White Sauce</p></div>

    <div class="contact">
      <p class="shop-name">Brelvo Pizza &amp; Pasta</p>
      <p class="contact-line"><svg viewBox="0 0 24 24" aria-hidden="true"><path d="M6.6 10.8a15.1 15.1 0 0 0 6.6 6.6l2.2-2.2a1 1 0 0 1 1-.25 11.4 11.4 0 0 0 3.6.57 1 1 0 0 1 1 1V20a1 1 0 0 1-1 1A17 17 0 0 1 3 4a1 1 0 0 1 1-1h3.5a1 1 0 0 1 1 1c0 1.25.2 2.45.57 3.57a1 1 0 0 1-.25 1z"/></svg>(03) 5550 1827</p>
      <p class="contact-line"><svg viewBox="0 0 24 24" aria-hidden="true"><path d="M12 2a7 7 0 0 0-7 7c0 5.25 7 13 7 13s7-7.75 7-13a7 7 0 0 0-7-7zm0 9.5A2.5 2.5 0 1 1 12 6.5a2.5 2.5 0 0 1 0 5z"/></svg>14 Harbour Lane, Eastport</p>
      <p class="contact-line">brelvopizza.example</p>
      <p class="note">Prices subject to change without notice</p>
    </div>
    <div class="photo photo-pasta" role="img" aria-label="Photo of a bowl of spaghetti pasta"></div>
  </section>

</main>
</body>
</html>
```